Mediation Website Design Upgrade

Project Details: https://files.plumvaro.net/sheet/k/8Wd3mPzqTuLhXe7nRaBo4_KcVy-92jsQ2fLgNwHd/view?ref=shared

Number of Pages Required

2 page

Font styles to use
Sans Serif

```html
<!DOCTYPE html>
<html lang="en">
<head>
<meta charset="utf-8">
<title>Harborline Mediation Group</title>
<link href="https://fonts.googleapis.com/css2?family=Rubik:wght@400;500&family=Montserrat:wght@500;600&display=swap" rel="stylesheet">
<style>
  :root{
    --white:#ffffff;
    --ink:#2b2b2b;
    --muted:#7a7a7a;
    --teal:#5b8884;
    --teal-dark:#4a7773;
    --teal-text:#4f8480;
    --menu-bg:#f5f8f7;
    --menu-hover:#e6eeec;
    --green:#6d9a3c;
    --strip:#e3e8e7;
    --footer-band:#e2eae8;
  }
  *{margin:0;padding:0;box-sizing:border-box}
  html,body{width:1200px;height:791px;overflow:hidden;background:var(--white)}
  body{position:relative;font-family:'Rubik',sans-serif;color:var(--ink)}

  .site-header{position:absolute;left:0;top:0;width:1200px;height:110px;background:var(--white)}
  .brand{position:absolute;left:253px;top:40px;display:flex;align-items:center;gap:7px}
  .brand-dot{width:14px;height:14px;border-radius:50%;background:var(--teal)}
  .brand-name{font-size:11px;font-weight:500;color:var(--ink);line-height:1.2;width:110px}
  .callback{position:absolute;left:456px;top:40px;display:flex;gap:12px;align-items:flex-start}
  .callback svg{margin-top:8px}
  .callback-label{font-size:7px;letter-spacing:1.3px;color:var(--muted)}
  .callback-number{font-size:14px;font-weight:500;color:var(--ink);margin-top:5px;letter-spacing:.3px}
  .top-links{position:absolute;top:52px;left:0;width:1200px;font-size:8px;font-weight:500}
  .top-links a{position:absolute;color:var(--ink);text-decoration:none}
  .top-links a.active{color:var(--green)}
  .top-underline{position:absolute;left:826px;top:72px;width:65px;height:2px;background:var(--green)}
  .header-strip{position:absolute;left:0;top:110px;width:1200px;height:6px;background:var(--strip)}

  .main-nav{position:absolute;left:0;top:116px;width:1200px;height:78px;background:var(--teal)}
  .main-nav .active-tab{position:absolute;left:401px;top:0;width:190px;height:78px;background:var(--teal-dark)}
  .main-nav a{position:absolute;top:33px;color:var(--white);font-size:9.5px;font-weight:500;text-decoration:none;letter-spacing:.2px}
  .main-nav svg{position:absolute;left:555px;top:36px}

  .hero{position:absolute;left:0;top:194px;width:1200px;height:578px;
    background:linear-gradient(100deg,#3a3d3e 0%,#55595a 35%,#6f7372 55%,#5d6161 75%,#4a4c4c 100%)}
  .hero-shade{position:absolute;inset:0;background:rgba(0,0,0,.18)}
  .hero-title{position:absolute;left:309px;top:126px;font-family:'Montserrat',sans-serif;font-weight:600;font-size:34px;color:var(--white);letter-spacing:.5px}
  .hero-subtitle{position:absolute;left:312px;top:214px;font-family:'Montserrat',sans-serif;font-weight:500;font-size:12.5px;color:var(--white)}
  .hero-rule{position:absolute;left:312px;top:242px;width:100px;height:2px;background:var(--green)}
  .hero-text{position:absolute;left:312px;top:268px;width:535px;font-size:11px;line-height:19px;color:var(--white)}
  .learn-more{position:absolute;left:751px;top:382px;width:136px;height:47px;background:var(--green);color:var(--white);
    font-size:8px;font-weight:500;letter-spacing:1.6px;display:flex;align-items:center;justify-content:center}
  .slider-arrow{position:absolute}
  .slider-dots{position:absolute;left:570px;top:517px;display:flex;gap:13px;align-items:center}
  .dot{width:10px;height:10px;border-radius:50%;background:#d8d8d8}
  .dot.current{width:14px;height:14px;border:2px solid #eee;background:transparent;position:relative}
  .dot.current::after{content:"";position:absolute;left:2px;top:2px;width:6px;height:6px;border-radius:50%;background:#eee}

  .dropdown{position:absolute;background:var(--menu-bg);box-shadow:0 4px 12px rgba(0,0,0,.15)}
  .dropdown .item{position:absolute;left:0;width:100%;font-size:9.5px;font-weight:500;color:var(--teal-text);padding-left:22px;display:flex;align-items:center}
  .dropdown .item.hover{background:var(--menu-hover)}
  .services-menu{left:401px;top:200px;width:190px;height:150px}
  .family-menu{left:597px;top:253px;width:190px;height:119px}

  .bottom-band{position:absolute;left:0;top:772px;width:1200px;height:19px;background:var(--footer-band)}
</style>
</head>
<body>
  <header class="site-header">
    <div class="brand"><span class="brand-dot"></span><span class="brand-name">Harborline Mediation Group</span></div>
    <div class="callback">
      <svg width="16" height="16" viewBox="0 0 24 24"><path d="M6.6 10.8a15.1 15.1 0 0 0 6.6 6.6l2.2-2.2a1 1 0 0 1 1-.25 11.4 11.4 0 0 0 3.6.57 1 1 0 0 1 1 1V20a1 1 0 0 1-1 1A17 17 0 0 1 3 4a1 1 0 0 1 1-1h3.5a1 1 0 0 1 1 1c0 1.25.2 2.45.57 3.6a1 1 0 0 1-.25 1z" fill="#2b2b2b"/></svg>
      <div>
        <div class="callback-label">WE WILL CALL YOU BACK</div>
        <div class="callback-number">555 - 014 - 2290</div>
      </div>
    </div>
    <nav class="top-links">
      <a style="left:785px">BLOG</a>
      <a class="active" style="left:836px">ABOUT US</a>
      <a style="left:907px">CONTACT</a>
    </nav>
    <div class="top-underline"></div>
  </header>
  <div class="header-strip"></div>

  <nav class="main-nav">
    <div class="active-tab"></div>
    <a style="left:336px">HOME</a>
    <a style="left:435px">MEDITATION SERVICES</a>
    <svg width="8" height="5" viewBox="0 0 8 5"><path d="M0 0h8L4 5z" fill="#fff"/></svg>
    <a style="left:634px">CONFLICT CONSULTING</a>
    <a style="left:814px">NEGOTIATION</a>
  </nav>

  <section class="hero">
    <div class="hero-shade" role="img" aria-label="Photo of two people seated at a table in a mediation meeting, one holding glasses"></div>
    <h1 class="hero-title">COMMERCIAL MEDIATION</h1>
    <h2 class="hero-subtitle">THE CATALYST FOR REVIVED COLLABORATION</h2>
    <div class="hero-rule"></div>
    <p class="hero-text">Commercial mediation addresses issues between two or more commercial enterprises and may also include solving conflicts within the same organization such as between different owners, executives, departments or employees. Commercial mediation can also address costly issues between firms and their service providers or suppliers</p>
    <div class="learn-more">LEARN MORE</div>
    <svg class="slider-arrow" style="left:92px;top:281px" width="14" height="18" viewBox="0 0 14 18"><path d="M10 2L3 9l7 7" stroke="#ddd" stroke-width="2" fill="none"/></svg>
    <svg class="slider-arrow" style="left:1079px;top:268px" width="42" height="42" viewBox="0 0 42 42"><circle cx="21" cy="21" r="20" stroke="rgba(255,255,255,.35)" stroke-width="1" fill="none"/><path d="M18 13l7 8-7 8" stroke="#ddd" stroke-width="2" fill="none"/></svg>
    <div class="slider-dots"><span class="dot"></span><span class="dot current"></span><span class="dot"></span></div>
  </section>

  <div class="dropdown services-menu">
    <div class="item" style="top:20px;height:28px">COMMERCIAL</div>
    <div class="item hover" style="top:53px;height:42px">FAMILY
      <svg style="position:absolute;left:160px" width="5" height="7" viewBox="0 0 5 7"><path d="M0 0l5 3.5L0 7z" fill="#4f8480"/></svg>
    </div>
    <div class="item" style="top:103px;height:28px">NONPROFITS</div>
  </div>

  <div class="dropdown family-menu">
    <div class="item" style="top:25px;height:28px">ELDER &amp; ADULT SIBLING</div>
    <div class="item hover" style="top:59px;height:42px">DIVORCE &amp; POST DIVORCE</div>
  </div>

  <div class="bottom-band"></div>
</body>
</html>
```